Card for invoking rights with police

Our criminal defense law firm is seeking proposals for a design for our card intended for clients to carry with them in their car. Upon being pulled over, they would hand this card to the officer.
Text for the back of the card:
"For Law Enforcement:"
"I will comply with lawful orders but respectfully decline any test or other requests without my attorney. I wish to remain silent, do not consent to searches, and request to speak with my attorney now.
The back of the card should prominently feature the text and the firm logo should be secondary.
Front
Must prominently feature contact info: 503-555-0182. Do not include attorney name, email, phone from the example file. This is intended to be generic for the firm and not tied to an individual lawyer.
Included for design reference: current business card, firm logo.
We intend to use trenvo.com to produce the cards.
Updates
The back of the card should prominently display the text regarding invocation of rights. Please title it "For Law Enforcement".
Target Market(s)
People who have been stopped by police
Contact Information for Business Card
see project description
Look and feel

```html
<!DOCTYPE html>
<html lang="en">
<head>
<meta charset="utf-8">
<title>Halvorsen Law Firm – Rights Card</title>
<link rel="stylesheet" href="https://fonts.googleapis.com/css2?family=Cinzel:wght@500;600&family=Lato:wght@400;700&display=swap">
<style>
  :root {
    --navy: #052f52;
    --white: #ffffff;
    --stage: #8f8f8f;
    --grey-text: #7a7a7a;
    --ink: #2b2b2b;
  }
  * { margin: 0; padding: 0; box-sizing: border-box; }
  html, body { width: 1039px; height: 1200px; overflow: hidden; }
  body { background: var(--stage); position: relative; font-family: "Lato", sans-serif; }

  .card { position: absolute; left: 124px; width: 783px; height: 446px; overflow: hidden; }
  .card--front { top: 93px; background: var(--white); }
  .card--back { top: 635px; background: var(--navy); color: var(--white); }

  /* Firm name */
  .firm-name { display: flex; align-items: center; gap: 18px; }
  .firm-name__square { background: var(--navy); flex: none; }
  .firm-name__text { font-family: "Cinzel", serif; font-weight: 500; color: var(--navy); line-height: 1.15; text-align: center; }
  .firm-name__text span { display: block; }

  .card--front .firm-name { position: absolute; left: 72px; top: 177px; }
  .card--front .firm-name__square { width: 49px; height: 63px; }
  .card--front .firm-name__text { font-size: 27px; letter-spacing: 0.08em; }
  .card--front .firm-name__text span { font-size: 15px; letter-spacing: 0.18em; }

  /* Front: firm contact */
  .main-phone { position: absolute; left: 419px; top: 118px; display: flex; align-items: center; gap: 14px;
    font-family: "Lato", sans-serif; font-weight: 700; font-size: 36px; color: var(--navy); letter-spacing: 0.02em; line-height: 1; }
  .main-phone svg { width: 26px; height: 26px; fill: var(--navy); flex: none; }
  .rule { position: absolute; left: 419px; right: 0; top: 178px; height: 1.5px; background: var(--navy); }

  .address { position: absolute; left: 419px; top: 200px; display: flex; align-items: flex-start; gap: 11px;
    font-size: 17px; line-height: 26px; color: var(--ink); }
  .address svg { width: 14px; height: 14px; margin-top: 6px; flex: none; fill: var(--navy); }

  .web-band { position: absolute; left: 0; bottom: 0; width: 755px; height: 39px; background: var(--navy); color: var(--white);
    font-size: 17px; letter-spacing: 0.32em; display: flex; align-items: center; justify-content: center; padding-left: 30px; }
  .corner-square { position: absolute; right: 0; bottom: 0; width: 28px; height: 39px; background: var(--navy); border: 3px solid var(--white); }

  /* Back */
  .card--back .firm-name { position: absolute; left: 0; right: 0; top: 52px; justify-content: center; gap: 14px; }
  .card--back .firm-name__square { width: 32px; height: 42px; background: var(--white); }
  .card--back .firm-name__text { color: var(--white); font-size: 22px; letter-spacing: 0.1em; }
  .card--back .firm-name__text span { font-size: 12px; letter-spacing: 0.18em; }

  .rights-title { position: absolute; left: 0; right: 0; top: 140px; text-align: center;
    font-family: "Cinzel", serif; font-weight: 600; font-size: 34px; letter-spacing: 0.06em; line-height: 1; }
  .rights-title::after { content: ""; display: block; width: 90px; height: 1.5px; background: var(--white); margin: 18px auto 0; }

  .rights-statement { position: absolute; left: 50%; top: 222px; width: 660px; transform: translateX(-50%);
    text-align: center; font-size: 21px; line-height: 33px; }
</style>
</head>
<body>

<section class="card card--front" aria-label="Card front">
  <div class="firm-name">
    <div class="firm-name__square"></div>
    <div class="firm-name__text">HALVORSEN<span>LAW FIRM</span></div>
  </div>

  <p class="main-phone">
    <svg viewBox="0 0 24 24" aria-hidden="true"><path d="M6.6 10.8a15 15 0 0 0 6.6 6.6l2.2-2.2c.3-.3.7-.4 1-.2 1.1.4 2.3.6 3.6.6.6 0 1 .4 1 1V20c0 .6-.4 1-1 1A17 17 0 0 1 3 4c0-.6.4-1 1-1h3.5c.6 0 1 .4 1 1 0 1.3.2 2.5.6 3.6.1.3 0 .7-.2 1z"/></svg>
    <span>503-555-0182</span>
  </p>
  <div class="rule"></div>

  <p class="address">
    <svg viewBox="0 0 24 24" aria-hidden="true"><path d="M12 1a8 8 0 0 0-8 8c0 6 8 14 8 14s8-8 8-14a8 8 0 0 0-8-8zm0 11a3 3 0 1 1 0-6 3 3 0 0 1 0 6z"/></svg>
    <span>1275 Cedar Crest Blvd NE<br>Suite 300, Brookvale, WA 98011</span>
  </p>

  <div class="web-band">www.halvorsenlawfirm.com</div>
  <div class="corner-square"></div>
</section>

<section class="card card--back" aria-label="Card back">
  <div class="firm-name">
    <div class="firm-name__square"></div>
    <div class="firm-name__text">HALVORSEN<span>LAW FIRM</span></div>
  </div>
  <h1 class="rights-title">For Law Enforcement:</h1>
  <p class="rights-statement">
    I will comply with lawful orders but respectfully decline any test or other requests without my attorney. I wish to remain silent, do not consent to searches, and request to speak with my attorney now.
  </p>
</section>

</body>
</html>
```